IT CEO and Real Estate Investor

It should include two roles and be a two sided card (both roles can be one a single side with a creative view or on different sides).
Card must be creative and interesting, but still professional.
Phone countries(USA/Russia) might be as flags or words, whatever works better.
Boris Melnovetz
Skype: boris_m
E-mail: melnovetz@quorbamail.com
Facebook: plavbook.example/melnovetz
Linkedin: trelnet.example/in/melnovetz
Phone (US): 1(555)316-2947
Phone (RUS): 7(955)482-3170
First role:
Pex Lattor (pexlattor.example) - include logo or part of logo (the $)
E-Commerce Automation Solutions
Founder/CEO/CTO
Second role:
Real Estate Investor
Cleveland, OH
UPDATE:
Let's do one side as logo only and all information on the other side - I don't like designs with information on both sides.
I also really liked designs on black (or other dark) background

```html
<!DOCTYPE html>
<html lang="en">
<head>
<meta charset="utf-8">
<title>Pex Lattor – Business Card</title>
<link href="https://fonts.googleapis.com/css2?family=Lexend:wght@400;500&family=Roboto:wght@400&display=swap" rel="stylesheet">
<style>
  :root {
    --backdrop: #e6e6e4;
    --card: #353130;
    --accent: #2aa7e0;
    --text-light: #f2f2f2;
    --shadow: rgba(0, 0, 0, 0.35);
  }
  * { box-sizing: border-box; margin: 0; padding: 0; }
  html, body {
    width: 1200px; height: 576px; overflow: hidden;
    background: var(--backdrop);
  }
  .stage { position: relative; width: 1200px; height: 576px; }
  .card {
    position: absolute; top: 139px;
    width: 484px; height: 292px;
    background: var(--card);
    border-radius: 6px;
    box-shadow: 2px 3px 6px var(--shadow);
    overflow: hidden;
  }
  .card--front { left: 82px; }
  .card--back { left: 602px; width: 480px; }

  /* Front: brand mark */
  .brand {
    position: absolute; inset: 0;
    display: flex; align-items: center; justify-content: center; gap: 16px;
  }
  .brand__dot {
    width: 44px; height: 44px; border-radius: 50%;
    background: var(--accent);
  }
  .brand__name {
    font-family: "Lexend", sans-serif; font-weight: 500;
    font-size: 27px; letter-spacing: 3px;
    color: var(--accent);
  }

  /* Back: details */
  .person {
    position: absolute; left: 0; right: 0; top: 62px;
    text-align: center; font-family: "Roboto", sans-serif;
  }
  .person__name {
    font-family: "Lexend", sans-serif; font-weight: 400;
    font-size: 30px; line-height: 36px;
    color: var(--accent); margin-bottom: 2px;
  }
  .person__role {
    font-size: 12px; line-height: 16px; color: var(--text-light);
  }
  .person__role .highlight { color: var(--accent); }

  .contacts {
    position: absolute; top: 187px;
    font-family: "Roboto", sans-serif; font-size: 13px; line-height: 17.5px;
    color: var(--text-light);
  }
  .contacts li { list-style: none; display: flex; align-items: center; height: 17.5px; white-space: nowrap; }
  .contacts--left { right: 244px; }
  .contacts--left li { justify-content: flex-end; }
  .contacts--left .icon { margin-left: 9px; }
  .contacts--right { left: 250px; }
  .contacts--right .icon { margin-right: 8px; }
  .icon { width: 12px; height: 12px; flex: none; display: block; }
  .icon--plain { width: 10px; height: 10px; background: var(--accent); border-radius: 2px; margin-left: 1px; }

  .accent-band {
    position: absolute; left: 0; right: 0; bottom: 0; height: 8px;
    background: var(--accent);
  }
</style>
</head>
<body>
<div class="stage">
  <section class="card card--front" aria-label="Card front">
    <div class="brand">
      <span class="brand__dot"></span>
      <span class="brand__name">PEX LATTOR</span>
    </div>
  </section>

  <section class="card card--back" aria-label="Card back">
    <div class="person">
      <h1 class="person__name">Boris Melnovetz</h1>
      <p class="person__role">E-Commerce Automation Solutions <span class="highlight">| Founder/CEO/CTO</span></p>
      <p class="person__role">Real Estate Investor <span class="highlight">| Cleveland, OH</span></p>
    </div>

    <ul class="contacts contacts--left">
      <li>(US): 1(555)316-2947
        <svg class="icon" viewBox="0 0 12 12" aria-hidden="true"><path fill="#2aa7e0" d="M1 4.5C1 2.5 3 1.5 6 1.5s5 1 5 3v1H8.5V4H3.5v1.5H1zM2.5 6.5l1.5-1.5h4l1.5 1.5V10.5h-7z"/><circle cx="6" cy="8" r="1.2" fill="#353130"/></svg>
      </li>
      <li>(RUS): 7(955)482-3170
        <svg class="icon" viewBox="0 0 12 12" aria-hidden="true"><path fill="#2aa7e0" d="M1 4.5C1 2.5 3 1.5 6 1.5s5 1 5 3v1H8.5V4H3.5v1.5H1zM2.5 6.5l1.5-1.5h4l1.5 1.5V10.5h-7z"/><circle cx="6" cy="8" r="1.2" fill="#353130"/></svg>
      </li>
      <li>melnovetz@quorbamail.com
        <svg class="icon" viewBox="0 0 12 12" aria-hidden="true"><rect x="0.5" y="2.5" width="11" height="7.5" fill="#2aa7e0"/><path d="M0.5 2.5L6 7l5.5-4.5" fill="none" stroke="#353130" stroke-width="1"/></svg>
      </li>
    </ul>

    <ul class="contacts contacts--right">
      <li><span class="icon icon--plain"></span>boris_m</li>
      <li><span class="icon icon--plain"></span>plavbook.example/melnovetz</li>
      <li><span class="icon icon--plain"></span>trelnet.example/in/melnovetz</li>
    </ul>

    <div class="accent-band"></div>
  </section>
</div>
</body>
</html>
```